Munchcart

App Design for a an application on which you can order take aways from restaurants close to you.
(similar app : https://appvault.example/lu/app/grubniq-pizza-burger-sushi/id583017264?l=en&mt=8 )

Logo is a taxi (psd of taxi an font attached)

Attached a draft mockup showing the screens needed.

Screens needed :

1. Splash Screen
2. Select you restaurant screen
3. Select your dish (meat, pizza, pasta....)
4. Select your extras (exta cheese, garlik etc...)
5. Exit screen with total amount and confirmation
6. Subscribe Screen where people have to register the first time.

Target Market(s)

age 14-54

Industry/Entity Type

Restaurant

Requirements
Must have
• Wood elements

```html
<!DOCTYPE html>
<html lang="en">
<head>
<meta charset="utf-8">
<title>Munchcart – App Screens</title>
<link href="https://fonts.googleapis.com/css2?family=Oswald:wght@400;500;600&family=Open+Sans:wdth,wght@75..100,400&display=swap" rel="stylesheet">
<style>
  :root {
    --stage: #d9d9db;
    --plank-a: #3a3a3a;
    --plank-b: #474747;
    --plank-c: #303030;
    --plank-seam: #161616;
    --tab-top: #2a2a2a;
    --tab-bottom: #050505;
    --tab-icon: #9a9a9a;
    --leather-light: #a56a40;
    --leather-dark: #86522c;
    --panel: #ffffff;
    --ink: #333333;
    --ink-soft: #555555;
    --field-border: #cfcfcf;
    --field-hint: #a5a5a5;
    --button: #7e4c2a;
    --button-edge: #5e361c;
    --on-brown: #f5ece3;
    --logo-ink: #121212;
    --taxi-yellow: #e4ae1e;
    --taxi-shade: #8a6414;
  }
  * { box-sizing: border-box; margin: 0; padding: 0; }
  html, body { width: 1200px; height: 1000px; overflow: hidden; }
  body {
    background: var(--stage);
    position: relative;
    font-family: "Open Sans", Arial, sans-serif;
  }

  .screen {
    position: absolute;
    top: 197px;
    width: 410px;
    height: 615px;
    overflow: hidden;
    background:
      linear-gradient(160deg, rgba(255,255,255,0) 45%, rgba(255,255,255,0.10) 55%, rgba(255,255,255,0) 70%),
      linear-gradient(180deg, rgba(0,0,0,0) 70%, rgba(0,0,0,0.25) 100%),
      repeating-linear-gradient(90deg,
        var(--plank-seam) 0px, var(--plank-seam) 2px,
        var(--plank-a) 2px, var(--plank-b) 22px, var(--plank-a) 44px,
        var(--plank-seam) 44px, var(--plank-seam) 46px,
        var(--plank-c) 46px, var(--plank-a) 70px, var(--plank-c) 94px,
        var(--plank-seam) 94px, var(--plank-seam) 96px,
        var(--plank-b) 96px, var(--plank-a) 118px, var(--plank-b) 142px);
  }
  .screen--splash { left: 113px; }
  .screen--find { left: 688px; }

  .tab-bar {
    position: absolute;
    left: 0; right: 0; bottom: 0;
    height: 64px;
    background: linear-gradient(180deg, var(--tab-top), var(--tab-bottom));
    border-top: 1px solid #3a3a3a;
  }
  .tab-icon {
    position: absolute;
    top: 16px;
    width: 30px; height: 30px;
    stroke: var(--tab-icon);
    fill: none;
    stroke-width: 2;
    stroke-linecap: round;
    stroke-linejoin: round;
  }
  .tab-icon--search { left: 77px; }
  .tab-icon--menu { left: 190px; }
  .tab-icon--cart { left: 294px; }

  /* Splash */
  .brand-name {
    position: absolute;
    top: 128px;
    left: 0; right: 0;
    text-align: center;
    font-family: "Oswald", Arial, sans-serif;
    font-weight: 600;
    font-size: 78px;
    line-height: 1;
    color: var(--logo-ink);
  }
  .taxi-art {
    position: absolute;
    left: 82px; top: 253px;
    width: 220px; height: 165px;
    border-radius: 46% 46% 30% 30% / 40% 40% 30% 30%;
    background: radial-gradient(ellipse at 55% 40%, var(--taxi-yellow) 0%, #cf9a1a 60%, var(--taxi-shade) 100%);
  }

  /* Find a restaurant */
  .find-header {
    position: absolute;
    left: 0; top: 6px;
    width: 408px; height: 70px;
    background: linear-gradient(180deg, var(--leather-light), var(--leather-dark));
    display: flex;
    align-items: center;
    justify-content: center;
  }
  .find-header::after {
    content: "";
    position: absolute;
    inset: 4px;
    border: 1px dashed rgba(255,255,255,0.22);
  }
  .find-title {
    font-family: "Oswald", Arial, sans-serif;
    font-weight: 500;
    font-size: 29px;
    letter-spacing: 1px;
    color: var(--on-brown);
  }
  .find-panel {
    position: absolute;
    left: 22px; top: 76px;
    width: 365px; height: 472px;
    background: linear-gradient(180deg, var(--panel) 0%, var(--panel) 36%, rgba(255,255,255,0.85) 60%, rgba(255,255,255,0.15) 100%);
  }
  .find-column { position: absolute; top: 25px; }
  .find-column--postcode { left: 22px; width: 150px; }
  .find-column--nearby { left: 209px; width: 130px; }
  .find-divider {
    position: absolute;
    left: 183px; top: 14px;
    height: 156px;
    border-left: 1px dashed #b5b5b5;
  }
  .column-title {
    font-size: 17px;
    font-weight: 400;
    color: var(--ink);
    line-height: 1.2;
  }
  .column-note {
    margin-top: 5px;
    font-size: 10.5px;
    font-stretch: 75%;
    line-height: 1.22;
    color: var(--ink-soft);
    height: 16px;
  }
  .find-column--nearby .column-note { height: auto; }
  .postcode-field {
    margin-top: 5px;
    width: 104px; height: 28px;
    border: 1px solid var(--field-border);
    border-radius: 4px;
    background: linear-gradient(180deg, #f1f1f1, #ffffff);
    font-size: 10.5px;
    font-stretch: 75%;
    color: var(--field-hint);
    padding: 6px 8px;
  }
  .find-button {
    display: flex;
    align-items: center;
    gap: 9px;
    height: 31px;
    padding: 0 10px;
    border-radius: 3px;
    background: var(--button);
    box-shadow: 0 2px 0 var(--button-edge);
    font-family: "Oswald", Arial, sans-serif;
    font-size: 16px;
    letter-spacing: 1.5px;
    color: var(--on-brown);
  }
  .find-column--postcode .find-button { margin-top: 16px; width: 80px; }
  .find-column--nearby .find-button { position: absolute; top: 95px; left: 0; width: 76px; }
  .button-icon {
    width: 15px; height: 15px;
    stroke: var(--on-brown);
    fill: none;
    stroke-width: 2.4;
    stroke-linecap: round;
  }
  .button-icon--arrow { fill: var(--on-brown); stroke: none; }
</style>
</head>
<body>

  <section class="screen screen--splash" aria-label="Splash screen">
    <div class="brand-name">Munchcart</div>
    <div class="taxi-art" role="img" aria-label="Illustration of a yellow vintage taxi cab"></div>
    <nav class="tab-bar">
      <svg class="tab-icon tab-icon--search" viewBox="0 0 30 30"><circle cx="12" cy="12" r="8"/><line x1="18" y1="18" x2="26" y2="26"/></svg>
      <svg class="tab-icon tab-icon--menu" viewBox="0 0 30 30"><path d="M9 4v8a3 3 0 0 0 6 0V4M12 4v24"/><path d="M21 28V4c-3 3-3 10 0 12"/></svg>
      <svg class="tab-icon tab-icon--cart" viewBox="0 0 30 30"><path d="M2 5h5l3 15h15l3-11H9"/><line x1="12" y1="13" x2="26" y2="13"/><line x1="16" y1="9" x2="16" y2="20"/><line x1="21" y1="9" x2="21" y2="20"/><circle cx="12" cy="25" r="2"/><circle cx="23" cy="25" r="2"/></svg>
    </nav>
  </section>

  <section class="screen screen--find" aria-label="Find a restaurant screen">
    <header class="find-header">
      <h1 class="find-title">FIND A RESTAURANT</h1>
    </header>
    <div class="find-panel">
      <div class="find-column find-column--postcode">
        <h2 class="column-title">My postcode</h2>
        <p class="column-note">Enter your postcode</p>
        <div class="postcode-field">eg. 388900</div>
        <div class="find-button">
          <svg class="button-icon" viewBox="0 0 16 16"><circle cx="6.5" cy="6.5" r="4.5"/><line x1="10" y1="10" x2="14.5" y2="14.5"/></svg>
          FIND
        </div>
      </div>
      <div class="find-divider"></div>
      <div class="find-column find-column--nearby">
        <h2 class="column-title">Nearby</h2>
        <p class="column-note">In order to activate this feature, don't forget to turn Location services on</p>
        <div class="find-button">
          <svg class="button-icon button-icon--arrow" viewBox="0 0 16 16"><path d="M15 1L1 7l6 2 2 6z"/></svg>
          FIND
        </div>
      </div>
    </div>
    <nav class="tab-bar">
      <svg class="tab-icon tab-icon--search" viewBox="0 0 30 30"><circle cx="12" cy="12" r="8"/><line x1="18" y1="18" x2="26" y2="26"/></svg>
      <svg class="tab-icon tab-icon--menu" viewBox="0 0 30 30"><path d="M9 4v8a3 3 0 0 0 6 0V4M12 4v24"/><path d="M21 28V4c-3 3-3 10 0 12"/></svg>
      <svg class="tab-icon tab-icon--cart" viewBox="0 0 30 30"><path d="M2 5h5l3 15h15l3-11H9"/><line x1="12" y1="13" x2="26" y2="13"/><line x1="16" y1="9" x2="16" y2="20"/><line x1="21" y1="9" x2="21" y2="20"/><circle cx="12" cy="25" r="2"/><circle cx="23" cy="25" r="2"/></svg>
    </nav>
  </section>

</body>
</html>
```